Golden Terrace Honey Labels

We are an importer and distributor in the UK of fine foods from Spain. We sell primarily to the retail and wholesale trade. I need a design for wrap around labels to put on jars for four different varieties of honey - Creamy Spring Blossom, Lavender, Wild Forest and Wild Thyme. The honey originates from Spain and will primarily be sold online and to independent retailers. The look and feeling I am looking for is classical, traditional, artisan and natural. I am looking for something simple and not too fussy. There needs to be an immediate obvious distinction on each label between the 4 varieties of honey, ideally by the use of different colours in some way in each design, though I would prefer the label background to be predominantly white. It is not necessary in the design to make it evident that it is from Spain. I have attached images of the jars and the honeys and also an image of the current label just for reference (but do not refer to the design). I have also attached the text for each variety of honey. The measurements for the labels are as follows: 167mm wide and 82mm high. Our logo will go on top of the lid of the jar. I really like the design I have attached to my brief. It is labelled 'Honey Design'.

Target Market(s)

Independent food retailers and online consumers

Industry/Entity Type

Fine Foods

Font styles to use
Script
Other font styles liked:
• Freeland Font for the word Honey

Requirements
Must have
• It needs to be immediately obvious by sight that each of the 4 varieties of honey are different
Nice to have
• Just the one same icon on each label for each variety of honey. Simple. Not too fussy. I really like the design attached labelled 'honey font'.

```html
<!DOCTYPE html>
<html lang="en">
<head>
<meta charset="UTF-8">
<title>Golden Terrace Honey Labels</title>
<link href="https://fonts.googleapis.com/css2?family=Domine:wght@400;700&family=Arimo:wght@400&display=swap" rel="stylesheet">
<style>
  :root{
    --page:#ffffff;
    --label:#f7f7f6;
    --ink:#2b2b2b;
    --spring:#e8902a;
    --spring-light:#f2c07a;
    --lavender:#7b4fa0;
    --lavender-light:#b89acb;
    --forest:#8a4422;
    --forest-light:#c9937a;
    --thyme:#c4a06a;
    --thyme-light:#e2cda8;
  }
  *{box-sizing:border-box;margin:0;padding:0}
  html,body{width:1200px;height:1200px;overflow:hidden;background:var(--page)}
  .range{
    width:1200px;height:1200px;
    display:flex;align-items:center;justify-content:center;gap:24px;
  }
  .label{
    --accent:var(--spring);--accent-light:var(--spring-light);
    width:270px;height:300px;background:var(--label);
    position:relative;display:flex;flex-direction:column;align-items:center;
    padding-top:28px;box-shadow:0 0 0 1px #e4e4e2;
    font-family:"Domine",serif;color:var(--ink);
  }
  .label--lavender{--accent:var(--lavender);--accent-light:var(--lavender-light)}
  .label--forest{--accent:var(--forest);--accent-light:var(--forest-light)}
  .label--thyme{--accent:var(--thyme);--accent-light:var(--thyme-light)}
  .claims{
    display:flex;align-items:center;gap:14px;
    font-size:7px;font-weight:700;letter-spacing:.02em;text-transform:uppercase;color:#444;
  }
  .claims .dot{width:12px;height:12px;border-radius:50%;background:var(--accent)}
  .brand{font-size:13px;font-weight:400;margin-top:6px;color:var(--ink)}
  .qualifier{font-size:15px;font-weight:700;margin-top:8px;height:18px}
  .variety{
    font-size:25px;font-weight:700;line-height:.98;text-align:center;
    color:var(--accent);text-transform:uppercase;
    height:58px;display:flex;flex-direction:column;justify-content:center;margin-top:4px;
  }
  .honey{font-size:34px;font-weight:700;line-height:1;margin-top:4px;letter-spacing:.01em}
  .comb{
    position:absolute;left:0;right:0;bottom:14px;height:100px;
    background:linear-gradient(90deg,var(--accent-light),var(--accent) 55%,var(--accent-light));
    opacity:.85;
  }
  .facts{position:absolute;bottom:24px;right:24px;text-align:center;color:#fff}
  .pure{font-size:9px;font-weight:700;line-height:1.2;margin-bottom:6px}
  .weight{font-family:"Arimo",sans-serif;font-size:9px;line-height:1.3}
  .weight b{font-size:12px;font-weight:400;display:block}
</style>
</head>
<body>
<main class="range">
  <section class="label label--spring">
    <div class="claims"><span>All Natural</span><span class="dot"></span><span>Hand Bottled</span></div>
    <p class="brand">Golden Terrace</p>
    <p class="qualifier">Creamy</p>
    <h2 class="variety"><span>Spring</span><span>Blossom</span></h2>
    <h1 class="honey">HONEY</h1>
    <div class="comb" role="img" aria-label="Honeycomb pattern in orange tones"></div>
    <div class="facts"><p class="pure">100%<br>PURE</p><p class="weight">Net.Wt:<b>450g</b></p></div>
  </section>
  <section class="label label--lavender">
    <div class="claims"><span>All Natural</span><span class="dot"></span><span>Hand Bottled</span></div>
    <p class="brand">Golden Terrace</p>
    <p class="qualifier"></p>
    <h2 class="variety"><span>Lavender</span></h2>
    <h1 class="honey">HONEY</h1>
    <div class="comb" role="img" aria-label="Honeycomb pattern in purple tones"></div>
    <div class="facts"><p class="pure">100%<br>PURE</p><p class="weight">Net.Wt:<b>450g</b></p></div>
  </section>
  <section class="label label--forest">
    <div class="claims"><span>All Natural</span><span class="dot"></span><span>Hand Bottled</span></div>
    <p class="brand">Golden Terrace</p>
    <p class="qualifier"></p>
    <h2 class="variety"><span>Wild</span><span>Forest</span></h2>
    <h1 class="honey">HONEY</h1>
    <div class="comb" role="img" aria-label="Honeycomb pattern in brown tones"></div>
    <div class="facts"><p class="pure">100%<br>PURE</p><p class="weight">Net.Wt:<b>450g</b></p></div>
  </section>
  <section class="label label--thyme">
    <div class="claims"><span>All Natural</span><span class="dot"></span><span>Hand Bottled</span></div>
    <p class="brand">Golden Terrace</p>
    <p class="qualifier"></p>
    <h2 class="variety"><span>Wild</span><span>Thyme</span></h2>
    <h1 class="honey">HONEY</h1>
    <div class="comb" role="img" aria-label="Honeycomb pattern in golden tan tones"></div>
    <div class="facts"><p class="pure">100%<br>PURE</p><p class="weight">Net.Wt:<b>450g</b></p></div>
  </section>
</main>
</body>
</html>
```